Mentorloft needs a WordPress - Design

I am a personal, team and business coach and help my clients to develop their potential. I mainly work with individuals and teams, but this can also be in the context of a company.
My business is called "Mentorloft"

The main goal of this website is to promote my business and to attire new customers.
I also want to present my concepts and ideas about coaching and how I actually do coaching and consulting. This is also to inform potential customers what coaching actually is and what it's not.
I want to host this website on a hosting-provider and want to be able to add and adapt content on my own. I'm thus looking for a WordPress - design.

Content:

vision
• Why do I do this
• How do I do this
• What am I doing

Coaching
• Career development
• Conflicts
• What is coaching, why coaching
• Conduct of a session and of the whole consultation
Limits of coaching
• Examples of positive effects of coaching

Support concept

Blog about current topics

Left

About me

Contact form

Footer / disclaimer

The following topics are the most important parts of my daily work as a coach with my clients, maybe this helps to get choos a suitable design:
- personality development, analyzing aspects and patterns and showing their influence
- Improve collaboration and cooperation in teams
- Addressing and solving conflicts (private and business)
- Identify and foster motivation, drivers, goals and action patterns
- Define next steps for the further improvement
- Accompany reorientation in professional career
- Discovering and using the strengths of the customers

The major part of my work is direct conversation with the customer, on site or virtually. My job is to support the customer in recognizing his own ideas, goals and possibilities and to define next steps in the desired direction

Target Market(s)

Small businesses and private persons in serch of a professional coach

Industry/Entity Type

Consultant

Number of Pages Required

1 page

Font styles to use
Sans Serif

Requirements
Must have
• - Logo / Name (see attachment)
- Menu, fixed navigation
- content
- blog
- Footer (contact, disclaimer)

- I need a WordPress design suitable for Mobile and Desktop devices.
- I'm looking for a modern, friendly and easy to use web site.
- First page as Long-pager (scrolling), other pages as long-pager or standard
- Decent, friendly colors but still clear, simple
Nice to have
• - Panorama image (image changing on every load of the site)
- Quote (changing on every load of the site)

```html
<!DOCTYPE html>
<html lang="en">
<head>
<meta charset="utf-8">
<title>Mentorloft – Personal, Team and Business Coaching</title>
<link rel="stylesheet" href="https://fonts.googleapis.com/css2?family=Poppins:wght@300;400;500;600&display=swap">
<style>
:root{
  --accent:#1ec0ea;
  --accent-deep:#2467c9;
  --ink:#1d1d1f;
  --muted:#555;
  --sand:#f4f2ee;
  --sand-light:#f8f6f2;
  --footer:#3c3c3e;
  --line:#d9d9d9;
  --navy:#2f3a8f;
}
*{box-sizing:border-box;margin:0;padding:0}
html,body{width:1200px;height:3898px;overflow:hidden}
body{position:relative;font-family:'Poppins',sans-serif;color:var(--ink);background:#fff}
.abs{position:absolute}

/* header */
.site-header{position:absolute;left:0;top:0;width:1200px;height:112px;background:#faf9f6}
.brand{left:80px;top:26px;display:flex;align-items:center;gap:14px}
.brand-mark{width:56px;height:56px;background:var(--navy)}
.brand-name{font-size:15px;letter-spacing:3px;color:var(--navy);font-weight:400}
.topline{right:95px;top:26px;display:flex;align-items:center;gap:22px;font-size:10px;color:#444}
.topline span{display:flex;align-items:center;gap:6px}
.dots{display:flex;gap:5px}
.dot{width:15px;height:15px;border:1.3px solid #333;border-radius:50%}
.main-nav{right:90px;top:65px;display:flex;gap:20px;font-size:11px;color:#333;letter-spacing:.2px}

/* hero */
.hero{left:0;top:112px;width:1200px;height:583px;background:linear-gradient(110deg,#4b4f55 0%,#8a8a8c 35%,#a9a7a4 55%,#6a6d72 80%,#4f5257 100%)}
.hero-title{left:85px;top:295px;font-size:64px;font-weight:300;color:#fff;letter-spacing:1px}
.hero-text{left:92px;top:398px;width:460px;font-size:15.5px;line-height:26px;color:#f1f1f1;font-weight:300}
.share-bar{right:0;top:276px;width:69px}
.share-bar div{height:69px;margin-bottom:1px}

/* features */
.features{left:0;top:695px;width:1200px;height:316px;background:var(--sand)}
.feature{width:260px;text-align:center;top:51px}
.feature .icon{width:84px;height:84px;border:1.6px solid #222;border-radius:50%;margin:0 auto 20px;display:flex;align-items:center;justify-content:center}
.feature h3{font-size:21px;font-weight:400;color:var(--accent);margin-bottom:14px}
.feature p{font-size:12px;line-height:21px;color:#444;width:200px;margin:0 auto}

/* about */
.about-heading{left:150px;top:1163px;font-size:42px;font-weight:400}
.about-name{left:148px;top:1256px;font-size:20px}
.about-role{left:148px;top:1286px;font-size:11.5px;font-weight:500}
.about-text{left:148px;top:1332px;width:340px;font-size:11.5px;line-height:20.5px;color:#444}
.about-link{left:148px;top:1512px;font-size:11.5px;color:var(--accent);text-decoration:underline}
.about-photo{left:646px;top:1137px;width:406px;height:406px;border-radius:50%;background:radial-gradient(circle at 50% 45%,#c89b84 0%,#a67a66 40%,#8d8a88 70%,#b4b2b0 100%)}

/* band */
.band{left:0;top:1655px;width:1200px;height:240px;background:linear-gradient(100deg,#1a9ccf 0%,#33b4dc 40%,#45bde3 70%,#29abe0 100%);text-align:center;color:#fff}
.band h2{position:absolute;left:0;right:0;top:50px;font-size:44px;font-weight:400}
.band p{position:absolute;left:280px;right:280px;top:131px;font-size:12.5px;line-height:21px;font-weight:500}

/* coaching */
.section-heading{left:0;width:1200px;text-align:center;font-size:44px;font-weight:400}
.coaching-list{left:133px;top:2142px;list-style:none;font-size:22px;line-height:41px}
.coaching-list li.plain{padding-left:14px}
.coaching-photo{left:727px;top:2142px;width:333px;height:254px;background:linear-gradient(90deg,#c4b49c 0%,#e4ddd2 45%,#eeeceb 70%,#9a7c68 100%)}

/* blog */
.blog{left:0;top:2545px;width:1200px;height:723px;background:var(--sand-light)}
.card{background:#fff}
.card h4{font-size:20px;font-weight:400;color:var(--accent)}
.meta{display:flex;gap:16px;font-size:12px;align-items:center}
.meta span{display:flex;align-items:center;gap:6px}
.card p{font-size:11.5px;line-height:21px;color:#555}
.card a{font-size:11.5px;color:var(--accent);text-decoration:underline}
.card-dark{background:linear-gradient(110deg,#1bb6ec 0%,#2a6fd2 100%);color:#fff}
.card-dark h4,.card-dark p,.card-dark a{color:#fff}

/* contact */
.field{height:44px;border:1px solid var(--line);font-size:11px;color:#aaa;padding:13px 16px;background:#fff}
.send-btn{left:494px;top:3557px;width:194px;height:44px;background:var(--accent);color:#fff;font-size:12px;display:flex;align-items:center;justify-content:center;gap:12px}

/* footer */
.site-footer{left:0;top:3684px;width:1200px;height:214px;background:var(--footer);color:#fff;font-size:12px}
.footer-name{left:0;width:1200px;top:96px;text-align:center;font-size:22px;letter-spacing:3px;color:#e6e6e6}
</style>
</head>
<body>

<header class="site-header">
  <div class="abs brand">
    <div class="brand-mark"></div>
    <div class="brand-name">MENTORLOFT</div>
  </div>
  <div class="abs topline">
    <span><svg width="12" height="9" viewBox="0 0 12 9"><rect x=".5" y=".5" width="11" height="8" fill="none" stroke="#333"/><path d="M.5 .5 6 5l5.5-4.5" fill="none" stroke="#333"/></svg>HELLO@MENTORLOFT.COM</span>
    <span><svg width="11" height="11" viewBox="0 0 24 24"><path d="M6.6 10.8a15 15 0 0 0 6.6 6.6l2.2-2.2a1 1 0 0 1 1-.25 11.4 11.4 0 0 0 3.6.6 1 1 0 0 1 1 1V20a1 1 0 0 1-1 1A17 17 0 0 1 3 4a1 1 0 0 1 1-1h3.5a1 1 0 0 1 1 1c0 1.25.2 2.450.6 3.6a1 1 0 0 1-.25 1z" fill="#333"/></svg>555 018 2040</span>
    <div class="dots"><div class="dot"></div><div class="dot"></div><div class="dot"></div></div>
  </div>
  <nav class="abs main-nav">
    <span>HOME</span><span>ABOUT ME</span><span>CHANGE YOUR LIFE</span><span>WORKSHOPS</span><span>SHOP</span><span>BLOG</span><span>CONTACT</span>
  </nav>
</header>

<section class="abs hero" role="img" aria-label="Blurred photo of a group coaching session"></section>
<h1 class="abs hero-title">Mentorloft</h1>
<p class="abs hero-text">Elias Brennan, a Latin professor at Ashford Hill College in Virginia, looked up one of the more obscure Latin words, consectetur, from</p>
<div class="abs share-bar" aria-label="Share buttons">
  <div style="background:#3b63b3"></div>
  <div style="background:#3aa5e6"></div>
  <div style="background:#1a76b8"></div>
</div>

<section class="abs features">
  <div class="abs feature" style="left:103px">
    <div class="icon"><svg width="44" height="40" viewBox="0 0 44 40" fill="none" stroke="#222" stroke-width="1.5"><rect x="4" y="4" width="30" height="22"/><path d="M10 22v-6M16 22v-9M22 22v-5M28 22v-11M19 26v10M12 36h14"/></svg></div>
    <h3>Why do I do this</h3>
    <p>Elias Brennan, a Latin professor at Ashford Hill College in Virginia</p>
  </div>
  <div class="abs feature" style="left:441px">
    <div class="icon"><svg width="44" height="44" viewBox="0 0 44 44" fill="none" stroke="#222" stroke-width="1.5"><circle cx="22" cy="22" r="15"/><circle cx="22" cy="22" r="6"/><path d="M22 4v5M22 35v5M4 22h5M35 22h5"/></svg></div>
    <h3>How do I do this</h3>
    <p>Elias Brennan, a Latin professor at Ashford Hill College in Virginia</p>
  </div>
  <div class="abs feature" style="left:760px">
    <div class="icon"><svg width="44" height="44" viewBox="0 0 44 44" fill="none" stroke="#222" stroke-width="1.5"><rect x="6" y="6" width="14" height="9" rx="2"/><rect x="24" y="14" width="16" height="22"/><path d="M4 38h36M12 20v16"/></svg></div>
    <h3>What am I doing</h3>
    <p>Elias Brennan, a Latin professor at Ashford Hill College in Virginia</p>
  </div>
</section>

<h2 class="abs about-heading">About Me</h2>
<div class="abs about-name">Jane Doe</div>
<div class="abs about-role">A personal mentor</div>
<p class="abs about-text">Elias Brennan, a Latin professor at Ashford Hill College in Virginia oked up one of the more obscure Latin words, consectetur, from a Lorem Ipsum passage, and going through the cites of the word in classical literature, discovered the<br><br>undoubtable source. Lorem Ipsum comes from sections 1.10.32 and 1.10.33 of</p>
<a class="abs about-link">More About Me</a>
<div class="abs about-photo" role="img" aria-label="Portrait photo of the coach"></div>

<section class="abs band">
  <h2>Examples of positive effects of coaching</h2>
  <p>Elias Brennan, a Latin professor at Ashford Hill College in Virginia oked up one of the more obscure Latin words, consectetur, from a Lorem Ipsum passage</p>
</section>

<h2 class="abs section-heading" style="top:1990px">Coaching</h2>
<ul class="abs coaching-list">
  <li>• Career development</li>
  <li>• Conflicts</li>
  <li>• What is coaching, why coaching</li>
  <li>• Conduct of a session and of the whole consultation</li>
  <li class="plain">Limits of coaching</li>
  <li>• Examples of positive effects of coaching</li>
</ul>
<div class="abs coaching-photo" role="img" aria-label="Photo of a coach talking with a client"></div>

<section class="abs blog"></section>
<h2 class="abs section-heading" style="top:2616px">Blog about current topics</h2>

<article class="abs card" style="left:127px;top:2738px;width:472px;height:433px">
  <div style="height:249px;background:linear-gradient(90deg,#3d3a36,#8d8a85 45%,#5a524a 100%)" role="img" aria-label="Photo of a workshop presentation"></div>
  <div style="padding:20px 27px">
    <h4 style="text-decoration:underline">Vivamus porta orci eu turpis vulputate</h4>
    <div class="meta" style="margin:12px 0 14px"><span>◯ admin</span><span>▭ 08/03/2016</span></div>
    <p>Elias Brennan, a Latin professor at Ashford Hill College in Virginia ne of the more obscure Latin words</p>
    <a style="display:block;margin-top:8px">More About Me</a>
  </div>
</article>

<article class="abs card card-dark" style="left:632px;top:2737px;width:428px;height:204px">
  <div class="abs" style="left:0;top:0;width:140px;height:204px;background:linear-gradient(120deg,#8a8884,#cfcac4 60%,#6e6862)" role="img" aria-label="Photo of a team celebrating"></div>
  <div class="abs" style="left:166px;top:30px;width:240px">
    <h4>Vivamus porta orci eu</h4>
    <div class="meta" style="margin:12px 0 14px"><span>◯ admin</span><span>▭ 08/03/2016</span></div>
    <p>Elias Brennan, a Latin professor at Ashford Hill</p>
    <a style="display:block;margin-top:8px">More About Me</a>
  </div>
</article>

<article class="abs card" style="left:632px;top:2971px;width:428px;height:204px">
  <div class="abs" style="left:0;top:0;width:140px;height:204px;background:linear-gradient(120deg,#b7b3ae,#e8e5e1 55%,#7f7a74)" role="img" aria-label="Photo of colleagues in an office"></div>
  <div class="abs" style="left:166px;top:30px;width:240px">
    <h4>Vivamus porta orci eu</h4>
    <div class="meta" style="margin:12px 0 14px"><span>◯ admin</span><span>▭ 08/03/2016</span></div>
    <p>Elias Brennan, a Latin professor at Ashford Hill</p>
    <a style="display:block;margin-top:8px">More About Me</a>
  </div>
</article>

<h2 class="abs section-heading" style="top:3322px">Contact Us</h2>
<div class="abs field" style="left:168px;top:3411px;width:260px">Your Name...</div>
<div class="abs field" style="left:462px;top:3411px;width:259px">Your Email...</div>
<div class="abs field" style="left:759px;top:3411px;width:260px">Your Phone...</div>
<div class="abs field" style="left:168px;top:3483px;width:851px">Message...</div>
<div class="abs send-btn">Send Message <span>›</span></div>

<footer class="abs site-footer">
  <div class="abs" style="left:170px;top:104px">Copyright © 2020 Mentorloft.</div>
  <div class="abs footer-name">MENTORLOFT</div>
  <div class="abs" style="left:858px;top:104px;display:flex;gap:14px;align-items:center">
    <span>Social Media</span>
    <div class="dots"><div class="dot" style="border-color:#fff"></div><div class="dot" style="border-color:#fff"></div><div class="dot" style="border-color:#fff"></div></div>
  </div>
</footer>

</body>
</html>
```